Business Card Design job - Tyre Shop

Client wants a double sided business cards designed for a Tyre Shop.

The logo can be used in multiple ways, some examples are attached.

The reference font is:
https://www.typebarrel.example/fonts/open-sans
Others can be applied.

Color scheme should be mainly black and white, and red as a third less used color.

Contact Information for Business Card

Required Fields (Portuguese language):
- Name "Artur Maldo"
- Title "Gerente"
- Phone "256 907 342"
- Website "www.rodalimpa.pt"
- Email "geral@rodalimpa.pt
- Address "Rua das Feiteiras N.187
4790-318 Quintela, Vizela"

Font styles to use
Sans Serif

Requirements
Must have
• Corporate Logo
Nice to have
• The client would like the card to have special feature to measure the tyre tread, as shown in examples attached.
• The tread Values as Portuguese law are:
• - Ilegal - less than 1.6mm
• - change tyres - between 3mm and 1.6 mm
• - OK - above 3mm
• Card should be kept standard rectangle size 85x55mm

```html
<!DOCTYPE html>
<html lang="pt">
<head>
<meta charset="utf-8">
<title>Roda Limpa – Cartão de visita</title>
<link rel="stylesheet" href="https://fonts.googleapis.com/css2?family=Open+Sans:wght@400;600;700;800&display=swap">
<style>
  :root {
    --backdrop: #2a2a2a;
    --card: #0c0c0c;
    --tread-tone: #1d1d1d;
    --white: #ffffff;
    --red: #e0242b;
    --band-text: #111111;
  }
  html, body {
    margin: 0;
    width: 1200px;
    height: 1200px;
    overflow: hidden;
    background: var(--backdrop);
    font-family: "Open Sans", Arial, sans-serif;
  }
  .sheet {
    position: relative;
    width: 1200px;
    height: 1200px;
  }
  .card {
    position: absolute;
    left: 190px;
    width: 820px;
    height: 530px;
    background: var(--card);
    box-shadow: 0 12px 30px rgba(0,0,0,0.5);
    overflow: hidden;
    color: var(--white);
  }
  .card--front { top: 50px; }
  .card--back  { top: 620px; }

  .tread-backdrop {
    position: absolute;
    left: -60px;
    top: -40px;
    width: 560px;
    height: 480px;
    border-radius: 50%;
    background: radial-gradient(ellipse at 55% 45%, var(--tread-tone) 0%, var(--tread-tone) 35%, rgba(29,29,29,0) 70%);
  }

  .brand-name {
    font-weight: 800;
    color: var(--white);
    text-transform: uppercase;
    line-height: 0.95;
    margin: 0;
  }
  .card--front .brand {
    position: absolute;
    left: 0; right: 0; top: 190px;
    text-align: center;
  }
  .card--front .brand-name { font-size: 64px; letter-spacing: 2px; }
  .card--front .front-web {
    position: absolute;
    left: 0; right: 0; bottom: 62px;
    text-align: center;
    color: var(--red);
    font-size: 22px;
    font-weight: 600;
    margin: 0;
  }

  .card--back .brand {
    position: absolute;
    left: 44px; top: 44px;
  }
  .card--back .brand-name { font-size: 50px; letter-spacing: 1px; }

  .contact {
    position: absolute;
    right: 44px; top: 112px;
    text-align: right;
    font-size: 18px;
    line-height: 1.35;
  }
  .contact__name {
    font-size: 30px;
    font-weight: 700;
    letter-spacing: 2px;
    text-transform: uppercase;
    margin: 0;
  }
  .contact__role {
    color: var(--red);
    font-size: 21px;
    font-weight: 600;
    letter-spacing: 2px;
    margin: 0 0 8px;
  }
  .contact__address { margin: 0 0 10px; }
  .contact__line {
    display: flex;
    justify-content: flex-end;
    align-items: center;
    gap: 10px;
  }
  .contact__line svg { width: 18px; height: 18px; flex: none; }

  .tread-legend {
    position: absolute;
    left: 0; right: 0; top: 328px;
    height: 34px;
    background: var(--white);
    color: var(--band-text);
    font-size: 18px;
    line-height: 34px;
    text-align: center;
    white-space: nowrap;
  }
  .tread-legend .dot { color: var(--red); }
  .tread-legend .illegal { color: var(--red); }

  .tread-gauge {
    position: absolute;
    left: 0; top: 362px;
    width: 820px;
    height: 168px;
  }
  .tread-gauge text {
    font-family: "Open Sans", Arial, sans-serif;
    font-size: 17px;
    fill: var(--white);
  }
  .tread-gauge .red-label { fill: var(--red); }
</style>
</head>
<body>
<main class="sheet">

  <section class="card card--front" aria-label="Frente do cartão">
    <div class="tread-backdrop" role="img" aria-label="Padrão suave de piso de pneu em fundo escuro"></div>
    <div class="brand"><p class="brand-name">Roda<br>Limpa</p></div>
    <p class="front-web">www.rodalimpa.pt</p>
  </section>

  <section class="card card--back" aria-label="Verso do cartão">
    <div class="brand"><p class="brand-name">Roda<br>Limpa</p></div>

    <div class="contact">
      <p class="contact__name">Artur Maldo</p>
      <p class="contact__role">GERENTE</p>
      <p class="contact__address">Rua das Feiteiras N.187<br>4790-318 Quintela, Vizela</p>
      <div class="contact__line">256 907 342
        <svg viewBox="0 0 24 24" fill="var(--red)" aria-hidden="true"><path d="M6.6 10.8a15.1 15.1 0 0 0 6.6 6.6l2.2-2.2c.3-.3.7-.4 1-.2 1.1.4 2.3.6 3.6.6.6 0 1 .4 1 1V20c0 .6-.4 1-1 1A17 17 0 0 1 3 4c0-.6.4-1 1-1h3.5c.6 0 1 .4 1 1 0 1.3.2 2.5.6 3.6.1.3 0 .7-.2 1z"/></svg>
      </div>
      <div class="contact__line">geral@rodalimpa.pt
        <svg viewBox="0 0 24 24" fill="var(--red)" aria-hidden="true"><path d="M2 5h20v14H2z"/><path d="M2 5l10 8 10-8" fill="none" stroke="var(--card)" stroke-width="2"/></svg>
      </div>
      <div class="contact__line">www.rodalimpa.pt
        <svg viewBox="0 0 24 24" fill="none" stroke="var(--red)" stroke-width="2" aria-hidden="true"><circle cx="12" cy="12" r="9"/><ellipse cx="12" cy="12" rx="4" ry="9"/><path d="M3 12h18M5 7h14M5 17h14"/></svg>
      </div>
    </div>

    <div class="tread-legend">
      Good : above 3mm <span class="dot">●</span> Change tyres : between 3mm and 1.6 mm <span class="dot">●</span> <span class="illegal">Ilegal : less than 1.6mm</span>
    </div>

    <svg class="tread-gauge" viewBox="0 0 820 168" aria-label="Medidor de profundidade do piso">
      <g transform="translate(0,12)">
        <g stroke="var(--white)" stroke-width="2">
          <line x1="0" y1="14" x2="800" y2="134"/>
          <line x1="0" y1="134" x2="820" y2="134"/>
          <line x1="30" y1="18" x2="30" y2="146"/>
          <line x1="126" y1="33" x2="126" y2="146"/>
          <line x1="222" y1="47" x2="222" y2="146"/>
          <line x1="319" y1="62" x2="319" y2="146"/>
          <line x1="415" y1="76" x2="415" y2="146"/>
          <line x1="511" y1="91" x2="511" y2="146"/>
          <line x1="607" y1="105" x2="607" y2="146"/>
          <line x1="704" y1="120" x2="704" y2="146"/>
        </g>
        <line x1="0" y1="128" x2="646" y2="128" stroke="var(--red)" stroke-width="2"/>
        <line x1="646" y1="100" x2="646" y2="146" stroke="var(--red)" stroke-width="2"/>
        <text x="22" y="10">8mm</text>
        <text x="120" y="25">7</text>
        <text x="216" y="39">6</text>
        <text x="313" y="54">5</text>
        <text x="409" y="68">4</text>
        <text x="495" y="83">3mm</text>
        <text x="601" y="97">2</text>
        <text class="red-label" x="652" y="90">1.6mm</text>
        <text x="712" y="114">1</text>
      </g>
    </svg>
  </section>

</main>
</body>
</html>
```